HTML Email Template

Hi,
I am looking to create a professional standardised email template. This is a basic html single page design, with my company details, logo and corporate colours etc, preferrably in a format suitable to email. Think a Outlook signature, but with a border around the email.
I will upload some basic samples, which will help to form the base of the design.

I just uploadedsome more files - 3 of them are logos (2 logos are the same, but I uploaded 2 sizes, please use whch is best)
I also uploaded another example (bad imaging I know) but the content of the page and the structure is what I want included also.
Thanks everyoine - Merry Christmas!

• must be editable, so I can edit the content of the emails.

```html
<!DOCTYPE html>
<html lang="en">
<head>
<meta charset="utf-8">
<title>Help Desk New Service Ticket Notification</title>
<link rel="stylesheet" href="https://fonts.googleapis.com/css2?family=Arimo:wght@400;700&family=Noto+Serif&family=PT+Sans&display=swap">
<style>
  :root {
    --page-grey: #8e929b;
    --paper: #ffffff;
    --header-blue-dark: #0d2f6e;
    --header-blue: #2a6fc4;
    --header-blue-light: #8fc3ee;
    --band-green: #8cc063;
    --title-blue: #3a5fcd;
    --link-blue: #1f4fc4;
    --ink: #1a1a1a;
    --label-ink: #2a2a2a;
    --row-a: #e7e9ee;
    --row-b: #f1f2f5;
    --footer-ink: #f2f3f6;
    --logo-ink: #2b2b2b;
  }
  * { box-sizing: border-box; margin: 0; padding: 0; }
  html, body { width: 1046px; height: 1200px; overflow: hidden; }
  body { background: var(--page-grey); font-family: "Arimo", Arial, sans-serif; color: var(--ink); position: relative; }

  .email { position: absolute; left: 133px; top: 0; width: 780px; }

  .masthead { position: relative; height: 223px; overflow: hidden;
    background: linear-gradient(100deg, var(--header-blue-dark) 0%, var(--header-blue) 55%, var(--header-blue-light) 100%); }
  .masthead-brand { position: absolute; left: 24px; top: 50px; color: #fff; font-size: 44px; font-weight: 400; letter-spacing: 1px; white-space: nowrap; }
  .masthead-tagline-small { position: absolute; left: 110px; top: 96px; color: #fff; font-size: 12px; white-space: nowrap; }
  .masthead-band { position: absolute; left: 0; top: 142px; width: 780px; height: 81px; background: var(--band-green); }
  .masthead-band p { position: absolute; left: 18px; top: 9px; font-family: "PT Sans", sans-serif; color: #fff; font-size: 22px; line-height: 29px; white-space: nowrap; }
  .masthead-photo { position: absolute; left: 380px; top: 0; width: 400px; height: 223px;
    background: linear-gradient(90deg, rgba(150,165,180,0) 0%, #9aa6b3 20%, #c8d7e6 60%, #a9c4df 100%); }
  .social { position: absolute; right: 10px; top: 8px; display: flex; gap: 6px; }
  .social span { width: 28px; height: 28px; border-radius: 4px; background: #dfe8f4; opacity: .9; }

  .content { background: var(--paper); height: 834px; position: relative; }
  .title { position: absolute; left: 49px; top: 34px; font-family: "Noto Serif", serif; font-weight: 400; font-size: 28px; color: var(--title-blue); letter-spacing: .3px; white-space: nowrap; }
  .greeting { position: absolute; left: 57px; top: 86px; font-size: 17px; font-weight: 700; }
  .body-copy { position: absolute; left: 57px; top: 122px; width: 700px; font-size: 14.5px; line-height: 26px; }
  .body-copy ul { margin-left: 22px; list-style: disc; }
  .body-copy li { line-height: 26.5px; }

  .signoff { position: absolute; left: 57px; top: 327px; font-size: 14.5px; line-height: 24px; }
  .signoff a { color: var(--link-blue); font-weight: 700; text-decoration: none; }
  .signoff-logo { position: absolute; left: 293px; top: 353px; font-size: 40px; color: var(--logo-ink); white-space: nowrap; }

  .section-heading { position: absolute; left: 58px; font-size: 16px; font-weight: 700; color: #333; }
  .ticket-table { position: absolute; left: 186px; width: 425px; border-collapse: separate; border-spacing: 0 2px; font-size: 14px; }
  .ticket-table th { width: 148px; text-align: left; padding-left: 20px; font-weight: 700; color: var(--label-ink); border-right: 2px solid #fff; white-space: nowrap; }
  .ticket-table td { padding-left: 14px; color: #333; white-space: nowrap; }
  .ticket-table tr { height: 37px; }
  .ticket-table tr:nth-child(odd) { background: var(--row-a); }
  .ticket-table tr:nth-child(even) { background: var(--row-b); }

  .footer { position: absolute; left: 165px; top: 1072px; color: var(--footer-ink); font-size: 12.5px; line-height: 19px; }
  .copyright { position: absolute; left: 165px; top: 1160px; color: var(--footer-ink); font-size: 12.5px; }
  .badge-partner { position: absolute; top: 1145px; height: 46px; border-radius: 3px; }
  .badge-partner.primary { left: 715px; width: 95px; background: linear-gradient(180deg, #2aa3e6, #0b6cc2); }
  .badge-partner.secondary { left: 821px; width: 70px; background: #f4f5f7; border: 2px solid #1f3f7a; }
</style>
</head>
<body>
  <div class="email">
    <header class="masthead">
      <div class="masthead-band"><p>Tech Support, Business<br>Technology and Cloud Solutions</p></div>
      <div class="masthead-photo" role="img" aria-label="Photo of a smiling IT consultant beside server towers"></div>
      <div class="masthead-brand">Corvane IT</div>
      <div class="masthead-tagline-small">your IT partner</div>
      <div class="social" aria-label="Social links"><span></span><span></span><span></span><span></span></div>
    </header>

    <main class="content">
      <h1 class="title">HELP DESK NEW SERVICE TICKET NOTIFICATION</h1>
      <p class="greeting">Dear [contactfirstname]:</p>
      <div class="body-copy">
        <p>We have received your email and ticket number <b>[srnumber],</b> related to "<b>[srsummary]</b>" has been created automatically.&nbsp; A technician will be working to address your issue shortly.</p>
        <p>Please reference the details listed below for more information.</p>
        <ul>
          <li>Error message &amp; user. Detailed error message with the issue and the name of the user.</li>
          <li>More details. Details of what the user was doing at the time</li>
          <li>Screen shots. Screen shots of your screen and/or error message.</li>
          <li>Screen name. Name of the screen and tab where the issue occurred</li>
        </ul>
      </div>

      <div class="signoff">
        Thank you,<br>
        MY COMPANY SUPPORT<br>
        <a href="mailto:support@corvaneit.co.nz">support@corvaneit.co.nz</a><br>
        <a href="#">www.corvaneit.co.nz</a>
      </div>
      <div class="signoff-logo">Corvane IT</div>

      <h2 class="section-heading" style="top:448px">SERVICE TICKET DETAIL</h2>
      <table class="ticket-table" style="top:478px">
        <tr><th>Ticket Number:</th><td>[srnumber]</td></tr>
        <tr><th>Ticket Status:</th><td>[srstatus]</td></tr>
        <tr><th>Ticket Summary:</th><td>[srsummary]</td></tr>
        <tr><th>Ticket Detail:</th><td>[srdetail]</td></tr>
      </table>

      <h2 class="section-heading" style="top:656px">SERVICE TICKET DETAIL</h2>
      <table class="ticket-table" style="top:692px">
        <tr><th>Account Name:</th><td>[companyname]</td></tr>
        <tr><th>Ticket Contact:</th><td>[contactfirstname] [contactlastname]</td></tr>
        <tr><th>Agreement Name:</th><td>[agrname]</td></tr>
      </table>
    </main>
  </div>

  <footer>
    <p class="footer">THIS NOTIFICATION WAS CREATED BY CORVANE IT SERVICES LTD HELP DESK SUPPORT TEAM<br>
      If you have any questions or wish to update information related to this ticket<br>
      simply reply to this email or call the help desk directly at 09-555-0142</p>
    <p class="copyright">Copyright © 2012 Corvane IT. All Rights Reserved.</p>
    <div class="badge-partner primary" aria-label="Partner badge"></div>
    <div class="badge-partner secondary" aria-label="Partner badge"></div>
  </footer>
</body>
</html>
```